Hello,

With my very limited web design knowledge I have designed my own websites...
Trailmerchant.org
Roverdealer.org

Whilst I have been very happy with the response I have received I feel the sites need enhancing. Here is what I would like to change..

1, Place a shadow around the whole pages outline so it has a 3d effect with a better background colour.

2, Improve the 'Request a valuation' tab so it stands out, maybe to also insert a curved arrow(s) to direct customer to click 'request a valuation' . Naturally this would need to be done on each page.

3, The testimonials of the 'what customers say' to change every few seconds.

4, The front page image to change every few seconds to a image of my choice.

5, any other suggestions you feel would benefit my site (obviously willing to pay extra for this and within this site)

6, given my limited knowledge my html code will surely need tidying also

7, if possible any changes not to affect my very good google ratings.

Price paid is for both sites as they're practically identical.

Thanks in advance

Gideon

```html
<!DOCTYPE html>
<html lang="en">
<head>
<meta charset="utf-8">
<title>Roverdealer.org – Sell your campervan</title>
<link href="https://fonts.googleapis.com/css2?family=Arimo:ital,wght@0,400;0,700;1,700&display=swap" rel="stylesheet">
<style>
:root{
  --backdrop:#ebe8e1;
  --page:#ffffff;
  --brand-blue:#3b7fc2;
  --teal:#1e9bc2;
  --nav-green:#3f6f14;
  --orange:#f08a24;
  --navy:#1b3c8c;
  --olive:#5b4f2c;
  --body-text:#333333;
  --footer-blue:#4a7ab8;
  --button-yellow:#fff59c;
  --button-border:#d8c85a;
  --bubble-orange:#f9c27b;
  --bubble-red:#ea5b5b;
  --bubble-blue:#a4aef2;
  --rule:#d9d3b8;
  --badge:#e4e4e4;
  --map-fill:#dfe2ec;
}
*{margin:0;padding:0;box-sizing:border-box}
html,body{width:1200px;height:2295px;overflow:hidden}
body{background:var(--backdrop);font-family:"Arimo",Arial,sans-serif;color:var(--body-text);position:relative}
.page{position:absolute;left:65px;top:9px;width:1054px;height:2286px;background:var(--page);box-shadow:0 0 28px 6px rgba(60,50,30,.35)}
.page > *{position:absolute}
.brand{left:17px;top:40px;font-size:48px;font-weight:700;color:var(--brand-blue);letter-spacing:-.5px}
.tagline{left:24px;top:91px;font-size:21px;color:#111}
.callout{left:734px;top:38px;font-size:17px;color:#222}
.callout strong{font-size:22px;color:var(--orange)}
.nav{left:480px;top:93px;width:570px;height:30px;font-size:21px;color:var(--nav-green)}
.nav span{position:absolute;top:0}
.nav-rule{left:55px;top:142px;width:651px;height:1px;background:var(--rule)}
.headline{left:60px;top:182px;font-size:31px;color:var(--teal)}
.valuation-button{left:105px;top:245px;width:486px;height:58px;border:1px solid var(--button-border);border-radius:9px;background:var(--button-yellow);box-shadow:0 2px 4px rgba(0,0,0,.25);font-size:25px;color:#111;display:flex;align-items:center;justify-content:center}
.valuation-button em{font-style:normal;color:#e3231e;margin:0 6px}
.pointer-arrow{left:590px;top:140px}
.cash-photo{left:768px;top:154px;width:210px;height:180px;background:linear-gradient(160deg,#f3ead0,#d9c38d 55%,#b49862)}
.hero-photo{left:0;top:342px;width:1054px;height:290px;background:linear-gradient(180deg,#9aa4b2 0%,#7b8a78 35%,#5c7a3a 65%,#3f5e2a 100%)}
.hero-label{left:27px;top:424px;font-size:130px;color:#fff;letter-spacing:-3px}
.hero-rule{left:0;top:647px;width:701px;height:1px;background:var(--rule)}
.benefits{left:65px;top:658px;list-style:none}
.benefits li{display:flex;align-items:center;height:44.5px;font-size:25px;color:var(--teal)}
.benefits svg,.side-heading svg{margin-right:12px;flex:none}
.intro{left:65px;top:908px;width:525px;font-size:20px;line-height:22.3px}
.intro p{margin-bottom:22.3px}
.caravan-photo{left:65px;top:1450px;width:561px;height:195px;background:linear-gradient(180deg,#b9c6d6 0%,#a8b9a0 40%,#6f8a4f 75%,#555f52 100%)}
.caravan-label{left:79px;top:1608px;font-size:22px;color:#fff}
.makes{left:52px;top:1717px;width:594px;height:417px}
.side-heading{left:734px;top:674px;display:flex;align-items:center;font-size:24px;color:#e0891f}
.coverage-note{left:734px;top:706px;width:250px;font-size:17px;line-height:22px;color:#222}
.towns{left:734px;top:770px;list-style:none;font-size:15px;line-height:17px;color:#111}
.map-graphic{left:840px;top:766px;width:144px;height:271px;background:var(--map-fill)}
.contact-title{left:710px;top:1086px;width:312px;text-align:center;font-size:25px;font-weight:700;color:var(--navy)}
.contact-email{left:710px;top:1114px;width:312px;text-align:center;font-size:24px;font-weight:700;color:var(--brand-blue)}
.reviews-heading{left:732px;top:1170px;width:250px;font-size:19.5px;line-height:24px;font-weight:700;color:var(--olive)}
.review{left:746px;width:253px;border-radius:14px;color:#fff;font-size:19px;line-height:22px;padding:24px 16px 0 13px;text-indent:18px}
.review::after{content:"";position:absolute;left:24px;bottom:-42px;border-style:solid;border-width:0 34px 42px 0;border-color:transparent;border-right-color:inherit}
.review .mark{position:absolute;font-size:44px;font-family:Georgia,serif;line-height:1;text-indent:0}
.review .open{left:8px;top:10px}
.review .close{right:10px;bottom:14px}
.review cite{display:block;margin-top:21px;font-style:italic;font-weight:700;text-indent:0}
.review cite span{display:block;padding-left:40px}
.review.orange{top:1234px;height:236px;background:var(--bubble-orange);border-color:var(--bubble-orange)}
.review.red{top:1544px;height:238px;background:var(--bubble-red);border-color:var(--bubble-red)}
.review.blue{top:1854px;height:241px;background:var(--bubble-blue);border-color:var(--bubble-blue)}
.footer{left:215px;top:2256px;width:450px;text-align:center;font-size:15px;color:var(--footer-blue)}
</style>
</head>
<body>
<div class="page">
  <div class="brand">Roverdealer.org</div>
  <div class="tagline">The UK's largest buyer of campervans</div>
  <div class="callout">Call us on <strong>0800 640 3182</strong></div>
  <nav class="nav">
    <span style="left:0">Home</span>
    <span style="left:122px">How it Works</span>
    <span style="left:309px">FAQ's</span>
    <span style="left:425px">Contact us</span>
  </nav>
  <div class="nav-rule"></div>

  <div class="headline">Sell your campervan quickly and securely</div>
  <div class="valuation-button">Request a <em>FREE</em> Valuation &gt;&gt;&gt;</div>
  <svg class="pointer-arrow" width="150" height="130" viewBox="0 0 150 130">
    <path d="M78 12 C130 20 145 60 110 90 C95 102 80 108 60 112" fill="none" stroke="#f08a24" stroke-width="20" stroke-linecap="round"/>
    <path d="M68 88 L20 114 L70 130 Z" fill="#f08a24"/>
  </svg>
  <div class="cash-photo" role="img" aria-label="Stack of banknotes"></div>

  <div class="hero-photo" role="img" aria-label="Painted landscape with lake, hills and a winding path"></div>
  <div class="hero-label">Photo 2</div>
  <div class="hero-rule"></div>

  <ul class="benefits">
    <li><svg width="24" height="22" viewBox="0 0 24 22"><path d="M2 12 L9 19 L22 3" fill="none" stroke="#f08a24" stroke-width="4"/></svg>Genuine online or verbal offer to purchase</li>
    <li><svg width="24" height="22" viewBox="0 0 24 22"><path d="M2 12 L9 19 L22 3" fill="none" stroke="#f08a24" stroke-width="4"/></svg>Excellent prices offered and paid</li>
    <li><svg width="24" height="22" viewBox="0 0 24 22"><path d="M2 12 L9 19 L22 3" fill="none" stroke="#f08a24" stroke-width="4"/></svg>No admin fees or hidden charges</li>
    <li><svg width="24" height="22" viewBox="0 0 24 22"><path d="M2 12 L9 19 L22 3" fill="none" stroke="#f08a24" stroke-width="4"/></svg>Friendly professional, no hassle service</li>
    <li><svg width="24" height="22" viewBox="0 0 24 22"><path d="M2 12 L9 19 L22 3" fill="none" stroke="#f08a24" stroke-width="4"/></svg>Instant cash or faster payment bank transfer</li>
  </ul>

  <div class="intro">
    <p>Selling your motorhome, campervan or American RV to roverdealer.org saves you the usual headaches and costs associated with selling a vehicle, not to mention the potential risks involved. All you need to do is either call us on the freephone number provided, or click the button above and complete our online request form with details of your motorhome or campervan. We will get back to you as soon as possible with a price and a no obligation offer to buy. If you accept our offer, we'll contact you to collect your motorhome at your convenience - free of charge.</p>
    <p>It is our aim to make the process of selling your motorhome completely straightforward and hassle-free. From your initial enquiry, to having your motorhome sold with money in your bank account or cash in your hand, can take less than 24 hours. We have even managed to complete some transactions the very same day the offer was received.</p>
    <p>Remember, there are no hidden charges for our service and you are not under any obligation to accept our offer. You really do have nothing to lose by simply finding out how much we can pay for your motorhome or campervan.</p>
  </div>

  <div class="caravan-photo" role="img" aria-label="Car towing a touring caravan along a country road"></div>
  <div class="caravan-label">Selling your Caravan?</div>

  <svg class="makes" viewBox="0 0 594 417" role="img" aria-label="Badges of vehicle makes we buy">
    <g fill="#e4e4e4">
      <rect x="10" y="8" width="60" height="60" rx="6"/><rect x="94" y="8" width="60" height="60" rx="6"/><rect x="178" y="8" width="60" height="60" rx="6"/><rect x="262" y="8" width="60" height="60" rx="6"/><rect x="346" y="8" width="60" height="60" rx="6"/><rect x="430" y="8" width="60" height="60" rx="6"/><rect x="514" y="8" width="60" height="60" rx="6"/>
      <rect x="10" y="92" width="60" height="60" rx="6"/><rect x="94" y="92" width="60" height="60" rx="6"/><rect x="178" y="92" width="60" height="60" rx="6"/><rect x="262" y="92" width="60" height="60" rx="6"/><rect x="346" y="92" width="60" height="60" rx="6"/><rect x="430" y="92" width="60" height="60" rx="6"/><rect x="514" y="92" width="60" height="60" rx="6"/>
      <rect x="10" y="176" width="60" height="60" rx="6"/><rect x="94" y="176" width="60" height="60" rx="6"/><rect x="178" y="176" width="60" height="60" rx="6"/><rect x="262" y="176" width="60" height="60" rx="6"/><rect x="346" y="176" width="60" height="60" rx="6"/><rect x="430" y="176" width="60" height="60" rx="6"/>
      <rect x="10" y="260" width="60" height="60" rx="6"/><rect x="94" y="260" width="60" height="60" rx="6"/><rect x="178" y="260" width="60" height="60" rx="6"/><rect x="262" y="260" width="60" height="60" rx="6"/><rect x="346" y="260" width="60" height="60" rx="6"/><rect x="430" y="260" width="60" height="60" rx="6"/><rect x="514" y="260" width="60" height="60" rx="6"/>
      <rect x="10" y="344" width="60" height="60" rx="6"/><rect x="94" y="344" width="60" height="60" rx="6"/><rect x="178" y="344" width="60" height="60" rx="6"/><rect x="262" y="344" width="60" height="60" rx="6"/><rect x="346" y="344" width="60" height="60" rx="6"/><rect x="430" y="344" width="60" height="60" rx="6"/><rect x="514" y="344" width="60" height="60" rx="6"/>
    </g>
  </svg>

  <div class="side-heading"><svg width="24" height="22" viewBox="0 0 24 22"><path d="M2 12 L9 19 L22 3" fill="none" stroke="#f08a24" stroke-width="4"/></svg>Free Collection</div>
  <div class="coverage-note">Below are some examples of of the areas we cover ...</div>
  <ul class="towns">
    <li>Birmingham</li><li>Cambridge</li><li>Chelmsford</li><li>Chichester</li><li>Chester</li><li>Exeter</li><li>Hertford</li><li>Leominster</li><li>Lincoln</li><li>Maidstone</li><li>Manchester</li><li>Norwich</li><li>Swansea</li><li>Truro</li><li>Wakefield</li>
  </ul>
  <div class="map-graphic" role="img" aria-label="Map of the United Kingdom"></div>

  <div class="contact-title">Contact Us</div>
  <div class="contact-email">info@roverdealer.org</div>
  <div class="reviews-heading">What our customers say....</div>

  <blockquote class="review orange">
    <span class="mark open">“</span>Many thanks for buying my Motorhome, I will have no hesitation in using you again or recommending you to family and friends.
    <cite>R. Holloway<span>- Ridgeway Tourer</span></cite>
    <span class="mark close">”</span>
  </blockquote>
  <blockquote class="review red">
    <span class="mark open">“</span>The whole transaction was smooth and very professionally undertaken. A good experience from start to finish.
    <cite>M. Farrant<span>- Kestrel Scout</span></cite>
    <span class="mark close">”</span>
  </blockquote>
  <blockquote class="review blue">
    <span class="mark open">“</span>Many thanks for buying my Motorhome, I will have no hesitation in using you again or recommending you to family and friends.
    <cite>R. Holloway<span>- Ridgeway Tourer</span></cite>
    <span class="mark close">”</span>
  </blockquote>

  <div class="footer">Roverdealer.org - Ashcombe Lane - Fenford - Essex CM99 2XZ</div>
</div>
</body>
</html>
```